Harborline Supply Company Business Card Design

The Business Card will be one side only with Harborline Supplies Company Logo
Card should have:
Name
Title
Office phone Number
Cell Number
email address
Website
Street Address
Our Slogan is Rugged and Reliable
Looking for something that stands out from other business cards

Target Market(s)

Heavy equipment Lease Company

```html
<!DOCTYPE html>
<html lang="en">
<head>
<meta charset="utf-8">
<title>Harborline Supplies Company — Business Card</title>
<link rel="stylesheet" href="https://fonts.googleapis.com/css2?family=Arimo:wght@400;700&display=swap">
<style>
  :root {
    --navy: #272873;
    --red: #d6202f;
    --white: #ffffff;
    --ink: #2b2b33;
    --backdrop: #e4ddd2;
  }
  * { margin: 0; padding: 0; box-sizing: border-box; }
  html, body { width: 1200px; height: 1200px; overflow: hidden; }
  body {
    background: var(--backdrop);
    font-family: "Arimo", Arial, sans-serif;
    position: relative;
  }
  .card {
    position: absolute;
    left: 240px;
    width: 720px;
    height: 412px;
    border-radius: 16px;
    overflow: hidden;
    box-shadow: 0 4px 10px rgba(0,0,0,0.18);
  }
  .card--front { top: 146px; background: var(--navy); }
  .card--back { top: 642px; background: var(--white); }

  .brand {
    position: absolute;
    left: 0; right: 0;
    display: flex;
    align-items: center;
    justify-content: center;
    gap: 16px;
  }
  .brand__dot {
    width: 22px; height: 22px;
    border-radius: 50%;
    background: var(--red);
  }
  .brand__name {
    font-weight: 700;
    font-size: 33px;
    letter-spacing: 0.5px;
    color: var(--red);
    white-space: nowrap;
  }
  .card--front .brand { top: 192px; }
  .card--front .brand__dot { background: var(--white); }
  .card--back .brand { top: 200px; }
  .card--back .brand__dot { background: var(--navy); }

  .slogan {
    position: absolute;
    left: 0; right: 0;
    top: 362px;
    text-align: center;
    color: var(--white);
    font-weight: 700;
    font-size: 19px;
    letter-spacing: 2.2px;
  }

  .contact {
    position: absolute;
    left: 26px;
    list-style: none;
    color: var(--ink);
    font-size: 17px;
    letter-spacing: 0.6px;
  }
  .contact li { display: flex; align-items: center; gap: 10px; height: 22px; }
  .contact svg { width: 14px; height: 14px; fill: var(--navy); flex: none; }
  .contact--phones { top: 27px; }
  .contact--web { top: 339px; }

  .person {
    position: absolute;
    right: 26px;
    top: 24px;
    text-align: right;
  }
  .person__name {
    color: var(--red);
    font-weight: 700;
    font-size: 27px;
    letter-spacing: 1.5px;
    line-height: 1.1;
  }
  .person__title { color: var(--ink); font-size: 17px; margin-top: 3px; }

  .address {
    position: absolute;
    right: 26px;
    top: 341px;
    text-align: right;
    font-style: normal;
    color: var(--ink);
    font-size: 15.5px;
    line-height: 20px;
    letter-spacing: 0.3px;
  }
</style>
</head>
<body>

<section class="card card--front" aria-label="Card front">
  <div class="brand">
    <span class="brand__dot"></span>
    <span class="brand__name">HARBORLINE SUPPLIES COMPANY</span>
  </div>
  <p class="slogan">RUGGED AND RELIABLE</p>
</section>

<section class="card card--back" aria-label="Card back">
  <ul class="contact contact--phones">
    <li>
      <svg viewBox="0 0 14 14" aria-hidden="true"><path d="M3.5 0h7a1 1 0 0 1 1 1v12a1 1 0 0 1-1 1h-7a1 1 0 0 1-1-1V1a1 1 0 0 1 1-1zm.8 1.5v6.5h5.4V1.5zm.3 8v1.2h1.2V9.5zm2 0v1.2h1.2V9.5zm2 0v1.2h1.2V9.5zm-4 2v1.2h1.2v-1.2zm2 0v1.2h1.2v-1.2zm2 0v1.2h1.2v-1.2z"/></svg>
      555 210 4478
    </li>
    <li>
      <svg viewBox="0 0 14 14" aria-hidden="true"><path d="M3 .5l2.2 2.8-1.3 1.6c.8 1.9 2.3 3.5 4.3 4.4l1.5-1.3L13.5 10l-1.3 2.6c-.4.7-1.2 1-2 .8C5.6 12.2 1.8 8.4.6 3.8.4 3 .8 2.2 1.5 1.8z"/></svg>
      555 318 2096
    </li>
  </ul>

  <div class="person">
    <p class="person__name">DANIEL WHITAKER</p>
    <p class="person__title">Director</p>
  </div>

  <div class="brand">
    <span class="brand__dot"></span>
    <span class="brand__name">HARBORLINE SUPPLIES COMPANY</span>
  </div>

  <ul class="contact contact--web">
    <li>
      <svg viewBox="0 0 14 14" aria-hidden="true"><path d="M0 2.5h14v9H0zm1.4 1.2L7 7.8l5.6-4.1z"/></svg>
      info@harborlinesupply.com
    </li>
    <li>
      <svg viewBox="0 0 14 14" aria-hidden="true"><path d="M7 0a7 7 0 1 0 0 14A7 7 0 0 0 7 0zm-.6 1.3v2.8H4.3c.5-1.5 1.2-2.5 2.1-2.8zm1.2 0c.9.3 1.6 1.3 2.1 2.8H7.6zM3.7 1.9c-.3.6-.6 1.4-.8 2.2H1.7a5.8 5.8 0 0 1 2-2.2zm6.6 0a5.8 5.8 0 0 1 2 2.2h-1.2c-.2-.8-.5-1.6-.8-2.2zM1.3 5.3h1.4c-.1.5-.1 1.1-.1 1.7H1.2c0-.6 0-1.2.1-1.7zm2.6 0h2.5V7H3.8c0-.6 0-1.2.1-1.7zm3.7 0h2.5c.1.5.1 1.1.1 1.7H7.6zm3.7 0h1.4c.1.5.1 1.1.1 1.7h-1.4c0-.6 0-1.2-.1-1.7zM1.2 8.2h1.4c0 .6.1 1.2.2 1.7H1.5c-.2-.5-.3-1.1-.3-1.7zm2.6 0h2.6v1.7H4c-.1-.5-.2-1.1-.2-1.7zm3.8 0h2.6c0 .6-.1 1.2-.2 1.7H7.6zm3.8 0h1.4c0 .6-.1 1.2-.3 1.7h-1.3c.1-.5.2-1.1.2-1.7zM2 11.1h1.1c.2.7.5 1.3.8 1.8A5.8 5.8 0 0 1 2 11.1zm2.4 0h2v2.6c-.8-.3-1.5-1.2-2-2.6zm3.2 0h2c-.5 1.4-1.2 2.3-2 2.6zm3.3 0H12a5.8 5.8 0 0 1-1.9 1.8c.3-.5.6-1.1.8-1.8z"/></svg>
      www.harborlinesupply.com
    </li>
  </ul>

  <address class="address">
    4120 N. Calloway PKWY Ste. B<br>
    Brenham, TX 77833
  </address>
</section>

</body>
</html>
```